Stand out flyer needed for Boxing gym

Hi we need a trifold brochure designed for our outdoor boxing business it will be delivered to doctors and nutritionists to help their patients be healthier and get fit.We have supplied high res pictures for you to use in the brochure. We need a design that use a lot of yellow so it captures their attention. You can check our website for design colours www.punchyard-fit.com.au

Target Market(s)

Overweight or unfit people looking to change their lives

Industry/Entity Type

Health And Wellness

Font styles to use
Sans Serif

Colors
fbee3d
ffffff
000000

Requirements
Must have
• (main heading - large bold font) Get fit lose weight & feel great
• (bold) Unlimited outdoor boxing classes $14.95
• Complete affordability & No judgements guaranteed
• (bold) Tailored programs (bold)
• Our programs are structured so that members of all fitness levels feel confident & comfortable during their start-up phase allowing you to quickly build your fitness
• (bold) Injury prevention (bold)
• Our training systems include techniques that will help you avoid injuries and build balanced strength
• (bold) Strengthen & Tone your core (bold)
• You're core muscles are some of you're most important muscles. Each workout you do incorporates core exercises to help avoid injuries and make you're total body stronger
• (bold) Wake up with more energy(bold)
• Every class you'll do will have you filled with energy the will pump you up for the rest of your day
• (bold) Sleep better(bold)
• One of the best parts of exercise is the benefit it has on your sleeping patterns. You'll sleep deeper & more sound
• (bold) Supportive environment (bold)
• At JAB YARD you'll be surrounded by trainers & other members who are there to encourage & motivate you to reach your goals and to get you moving more.
• Coupon code: SwingHigh27

```html
<!DOCTYPE html>
<html lang="en">
<head>
<meta charset="utf-8">
<title>Jab Yard Trifold Brochure</title>
<link href="https://fonts.googleapis.com/css2?family=Montserrat:wght@400;500;700&family=Rubik:wght@700;800;900&display=swap" rel="stylesheet">
<style>
  :root {
    --yellow: #fbee3d;
    --black: #000000;
    --white: #ffffff;
    --ink: #1a1a1a;
    --stage: #e4e4e4;
    --heading: "Rubik", Arial, sans-serif;
    --body: "Montserrat", Arial, sans-serif;
  }
  * { box-sizing: border-box; margin: 0; padding: 0; }
  html, body { width: 900px; height: 1200px; overflow: hidden; background: var(--stage); }
  .canvas { position: relative; width: 900px; height: 1200px; }

  .sheet {
    position: absolute; left: 30px; width: 840px; height: 560px;
    display: flex; box-shadow: 0 6px 18px rgba(0,0,0,.18);
  }
  .sheet--outside { top: 30px; }
  .sheet--inside { top: 615px; }
  .panel { position: relative; width: 280px; height: 560px; overflow: hidden; background: var(--white); }
  .panel + .panel { border-left: 1px solid rgba(0,0,0,.06); }

  .shape, .photo { position: absolute; }
  .fill-yellow { background: var(--yellow); }
  .fill-black { background: var(--black); }

  .photo-gym { background: linear-gradient(160deg, #5d6066 0%, #2c2e33 60%, #8c8577 100%); }
  .photo-faint { background: linear-gradient(180deg, rgba(120,120,120,.18), rgba(200,200,200,.08)); }
  .photo-park { background: linear-gradient(170deg, #c9b98a 0%, #5f7a3c 55%, #364a22 100%); }
  .photo-highfive { background: linear-gradient(150deg, #b8a27a 0%, #7f9b4e 50%, #3d5a26 100%); }
  .photo-trainer { background: linear-gradient(160deg, #c98f6a 0%, #5b6f8c 55%, #2b3547 100%); }

  .body-text { font-family: var(--body); font-size: 10px; line-height: 1.42; color: var(--ink); }
  .title { font-family: var(--heading); font-weight: 900; line-height: 1; }

  /* wordmark */
  .wordmark { position: absolute; display: flex; align-items: center; gap: 7px; }
  .wordmark__square { width: 12px; height: 12px; }
  .wordmark__name { font-family: var(--heading); font-weight: 800; font-size: 24px; letter-spacing: 1px; }

  /* back panel */
  .back__content { position: absolute; inset: 18px 20px; }
  .back__band { background: var(--black); color: var(--yellow); font-family: var(--heading); font-weight: 800; font-size: 15px; padding: 6px 10px; margin: 0 -20px 8px; padding-left: 20px; }
  .back__para { margin-bottom: 9px; }
  .marker-heading { display: flex; align-items: center; gap: 6px; font-family: var(--heading); font-weight: 800; font-size: 15px; color: var(--black); margin: 4px 0 5px; }
  .marker-heading::before { content: ""; width: 10px; height: 16px; background: var(--black); flex: none; }

  /* promo panel */
  .promo__offer { position: absolute; left: 22px; right: 18px; top: 165px; text-align: center; }
  .promo__lead { color: var(--yellow); font-size: 38px; }
  .promo__classes { color: var(--white); font-size: 21px; margin-top: 4px; }
  .promo__price { color: var(--yellow); }
  .promo__note { color: var(--white); font-family: var(--heading); font-weight: 700; font-size: 11px; margin-top: 8px; line-height: 1.25; }
  .promo__contact { position: absolute; right: 22px; bottom: 34px; text-align: right; color: var(--white); font-family: var(--body); font-weight: 700; font-size: 10.5px; line-height: 1.55; }
  .promo__contact .wordmark { position: static; justify-content: flex-end; margin-bottom: 6px; }

  /* cover */
  .cover__headline { position: absolute; left: 22px; right: 14px; bottom: 60px; color: var(--black); }
  .cover__big { font-size: 60px; letter-spacing: -1px; }
  .cover__sub { font-size: 22px; margin-top: 4px; }
  .glove-mark { position: absolute; border-radius: 50%; background: var(--white); }

  /* inside */
  .feature { position: absolute; left: 0; right: 0; }
  .feature__band { background: var(--yellow); font-family: var(--heading); font-weight: 800; font-size: 15px; padding: 4px 18px; color: var(--black); }
  .feature__list { padding: 6px 18px 0 18px; }
  .feature__list .body-text { margin-bottom: 8px; }
  .energy { position: absolute; left: 90px; right: 14px; top: 30px; color: var(--white); }
  .energy__title { font-size: 17px; line-height: 1.05; }
  .energy__text { font-family: var(--body); font-size: 8.5px; line-height: 1.35; margin-top: 5px; }
  .benefits { position: absolute; left: 18px; right: 16px; top: 20px; }
  .benefits__title { font-family: var(--heading); font-weight: 800; font-size: 15px; color: var(--black); margin-bottom: 3px; }
  .benefits .body-text { margin-bottom: 9px; font-size: 9.5px; }
  .coupon { text-align: right; font-family: var(--heading); font-weight: 800; font-size: 15px; line-height: 1.1; }
  .coupon__code { display: block; font-size: 12px; }
</style>
</head>
<body>
<main class="canvas">

  <!-- Outside of the trifold -->
  <section class="sheet sheet--outside">

    <article class="panel back">
      <div class="photo photo-faint" style="inset:0" role="img" aria-label="Faint photo of a boxer training"></div>
      <div class="back__content">
        <h2 class="back__band">Find Your Toughness</h2>
        <p class="body-text back__para">What's the difference between successful people and the rest? Toughness! Not just physically but mentally as well. Everyday you face pressure, struggles and choices. No one can do it for you. You must dig deep and find your inner toughness. That primal instinct inside you to not just survive but to thrive.</p>
        <p class="body-text back__para">We guarentee every session you complete will have you both mentally and physically tougher ready to take on the tough challenges &amp; decisions you face everyday.</p>
        <h2 class="marker-heading">Jab Yard Culture</h2>
        <p class="body-text back__para">Some days you just don't feel like getting back up and it's those days you need to be surrounded by people. Not just your friends. Not just your family. But people who want you to reach your goals as much as they want to reach their own. People who feel that your success is in turn their success.</p>
        <p class="body-text back__para">This is what Jab Yard is all about. We employ the best coaches who have a passion for seeing you succeed &amp; our members strive to help their teammates achieve everything they set their minds on.</p>
      </div>
    </article>

    <article class="panel promo fill-black">
      <div class="photo photo-gym" style="inset:0 0 300px 0;opacity:.25" role="img" aria-label="Dark photo of a boxer in the background"></div>
      <div class="shape fill-yellow" style="inset:0;clip-path:polygon(45% 0,100% 0,100% 32%)"></div>
      <div class="shape fill-black" style="inset:0;clip-path:polygon(100% 0,100% 40%,60% 0)"></div>
      <div class="shape fill-yellow" style="inset:0;clip-path:polygon(0 56%,0 100%,40% 100%)"></div>
      <div class="shape fill-yellow" style="inset:0;clip-path:polygon(18% 100%,72% 100%,48% 78%)"></div>
      <div class="promo__offer">
        <h1 class="title promo__lead">Unlimited</h1>
        <p class="title promo__classes">Outdoor Boxing Classes <span class="promo__price">$14.95</span></p>
        <p class="promo__note">Complete Affordability &amp;<br>No Judgements Guaranteed</p>
      </div>
      <div class="promo__contact">
        <div class="wordmark"><span class="wordmark__square fill-yellow"></span><span class="wordmark__name" style="color:var(--white)">JAB YARD</span></div>
        <p>0412 555 019</p>
        <p>info@punchyard-fit.com.au</p>
        <p>www.punchyard-fit.com.au</p>
      </div>
    </article>

    <article class="panel cover">
      <div class="photo photo-gym" style="left:70px;right:20px;top:60px;height:190px" role="img" aria-label="Photo of a hooded boxer in front of a city skyline"></div>
      <div class="shape fill-black" style="inset:0;clip-path:polygon(100% 10%,100% 55%,45% 40%)"></div>
      <div class="glove-mark" style="left:190px;top:150px;width:56px;height:56px" role="img" aria-label="Boxing gloves icon"></div>
      <div class="shape fill-yellow" style="inset:0;clip-path:polygon(0 62%,50% 40%,100% 55%,100% 100%,0 100%)"></div>
      <div class="wordmark" style="left:26px;top:22px"><span class="wordmark__square fill-black"></span><span class="wordmark__name">JAB YARD</span></div>
      <div class="cover__headline">
        <h1 class="title cover__big">Get<br>Fit Lose</h1>
        <p class="title cover__sub">Weight &amp; Feel Great</p>
      </div>
    </article>
  </section>

  <!-- Inside of the trifold -->
  <section class="sheet sheet--inside">

    <article class="panel features">
      <div class="photo photo-park" style="left:0;right:0;top:0;height:190px" role="img" aria-label="Photo of people doing planks on grass at sunset"></div>
      <div class="photo photo-faint" style="left:0;right:0;top:190px;bottom:0" role="img" aria-label="Faint photo of an outdoor workout"></div>
      <div class="feature" style="top:205px">
        <h2 class="feature__band">Tailored Programs</h2>
        <div class="feature__list">
          <p class="body-text">Our programs are structured so that members of all fitness levels feel confident &amp; comfortable during their start-up phase allowing you to quickly build your fitness</p>
          <h2 class="marker-heading">Injury Prevention</h2>
          <p class="body-text">Our training systems include techniques that will help you avoid injuries and build balanced strength</p>
          <h2 class="marker-heading">Strengthen &amp; Tone Your Core</h2>
          <p class="body-text">You're core muscles are some of you're most important muscles. Each workout you do incorporates core exercises to help avoid injuries and make you're total body stronger</p>
        </div>
      </div>
    </article>

    <article class="panel energy-panel">
      <div class="photo photo-highfive" style="inset:0" role="img" aria-label="Photo of a smiling woman giving a high five outdoors"></div>
      <div class="shape fill-black" style="inset:0;clip-path:polygon(0 0,100% 0,100% 8%,100% 20%,25% 36%,0 14%)"></div>
      <div class="shape fill-yellow" style="inset:0;clip-path:polygon(0 0,22% 0,0 13%)"></div>
      <div class="shape fill-yellow" style="inset:0;clip-path:polygon(100% 58%,100% 100%,55% 100%)"></div>
      <div class="energy">
        <h2 class="title energy__title">Wake Up With<br>More Energy</h2>
        <p class="energy__text">Every class you'll do will have you filled with energy the will pump you up for the rest of your day</p>
      </div>
    </article>

    <article class="panel support">
      <div class="photo photo-trainer" style="inset:0" role="img" aria-label="Photo of a smiling trainer holding a tablet in a gym"></div>
      <div class="shape fill-yellow" style="inset:0;clip-path:polygon(0 0,100% 0,100% 30%,0 44%)"></div>
      <div class="shape fill-black" style="inset:0;clip-path:polygon(0 72%,45% 100%,0 100%)"></div>
      <div class="shape fill-black" style="inset:0;clip-path:polygon(15% 100%,100% 66%,100% 100%)"></div>
      <div class="shape fill-yellow" style="inset:0;clip-path:polygon(0 60%,30% 100%,0 100%)"></div>
      <div class="benefits">
        <h2 class="benefits__title">Sleep better</h2>
        <p class="body-text">One of the best parts of exercise is the benefit it has on your sleeping patterns. You'll sleep deeper &amp; more sound</p>
        <h2 class="benefits__title">Supportive Environment</h2>
        <p class="body-text">At JAB YARD you'll be surrounded by trainers &amp; other members who are there to encourage &amp; motivate you to reach your goals and to get you moving more.</p>
        <p class="coupon">Coupon Code <span class="coupon__code">SwingHigh27</span></p>
      </div>
    </article>
  </section>

</main>
</body>
</html>
```